"Harrow Crest Builders" is a residential building company and needs a new business card design and may re

We would like a redesign based on the existing logo, and would like to see a new font as well. We are bespoke home builders who build sustainable energy efficient homes.

Industry/Entity Type

Construction

Contact Information for Business Card

Business card size 40mm x 90mm

Colors

Designer to choose colors to be used in the design.

```html
<!DOCTYPE html>
<html lang="en">
<head>
<meta charset="utf-8">
<title>Harrow Crest Builders – Business Card</title>
<link rel="stylesheet" href="https://fonts.googleapis.com/css2?family=Arimo:wght@400;700&family=Montserrat:wght@400&display=swap">
<style>
  :root {
    --backdrop: #e9e9ea;
    --card: #414652;
    --card-deep: #363b47;
    --ink: #cfbba8;
    --ink-soft: #c2b3a6;
  }
  * { box-sizing: border-box; margin: 0; padding: 0; }
  html, body {
    width: 1200px;
    height: 1200px;
    overflow: hidden;
    background: var(--backdrop);
  }
  .canvas {
    position: relative;
    width: 1200px;
    height: 1200px;
  }
  .card {
    position: absolute;
    width: 700px;
    height: 400px;
    background: linear-gradient(120deg, var(--card) 0%, #4a4f5a 45%, var(--card-deep) 100%);
    box-shadow: 0 6px 18px rgba(0, 0, 0, 0.12);
    color: var(--ink);
  }
  .card--front { left: 330px; top: 130px; }
  .card--back  { left: 170px; top: 670px; }

  .brand {
    position: absolute;
    left: 200px;
    top: 130px;
    display: flex;
    align-items: center;
    gap: 26px;
  }
  .brand__square {
    width: 70px;
    height: 70px;
    background: var(--ink);
  }
  .brand__name {
    font-family: "Montserrat", sans-serif;
    font-weight: 400;
    font-size: 46px;
    line-height: 1.15;
    letter-spacing: 0.06em;
    color: var(--ink);
  }

  .holder {
    position: absolute;
    left: 70px;
    top: 210px;
    font-family: "Arimo", sans-serif;
    font-weight: 700;
    font-size: 38px;
    line-height: 1.12;
    color: var(--ink);
  }
  .details {
    position: absolute;
    left: 320px;
    top: 80px;
    font-family: "Arimo", sans-serif;
    font-weight: 400;
    font-size: 17px;
    line-height: 1.35;
    color: var(--ink-soft);
    list-style: none;
  }
  .details__group + .details__group { margin-top: 18px; }
</style>
</head>
<body>
<main class="canvas">
  <section class="card card--front" aria-label="Card front">
    <div class="brand">
      <span class="brand__square" aria-hidden="true"></span>
      <p class="brand__name">Harrow Crest<br>Builders</p>
    </div>
  </section>

  <section class="card card--back" aria-label="Card back">
    <p class="holder">Daniel<br>Moretti</p>
    <ul class="details">
      <li class="details__group">0412 555 018</li>
      <li class="details__group">daniel@harrowcrestbuilders.com.au<br>www.harrowcrestbuilders.com.au</li>
      <li class="details__group">PO Box 2178 Northgate LPO<br>Kelford WA 6099</li>
      <li class="details__group">Registration 40583<br>ABN: 52 304 771 068</li>
    </ul>
  </section>
</main>
</body>
</html>
```